M&A Advisory firm needs elegant and powerful letterhead

We need a powerful but elegant letterhead to engage with the international financial industry.

Target Market(s)

New York and International Financial Industry

Industry/Entity Type

Finance

Font styles to use
Other font styles liked:
• Poppins

Requirements
Must have
• 482 W 71st Street 14th Floor New York, NY 10157 O: +1 (212) 555 0147 F: +1 (212) 555 0182

```html
<!DOCTYPE html>
<html lang="en">
<head>
<meta charset="utf-8">
<title>Halvern Letterhead</title>
<link rel="stylesheet" href="https://fonts.googleapis.com/css2?family=Poppins:wght@400&family=PT+Sans:wght@400;700&family=Nothing+You+Could+Do&display=swap">
<style>
  :root {
    --brand-blue: #0a4d99;
    --brand-grey: #9a9a9c;
    --soft-grey: #dedee0;
    --ink: #2d2d2f;
    --body-ink: #7a7a7c;
    --signature-ink: #1d2a6b;
    --backdrop: #ececee;
    --paper: #ffffff;
  }
  * { box-sizing: border-box; margin: 0; padding: 0; }
  html, body { width: 1200px; height: 795px; overflow: hidden; }
  body { background: var(--backdrop); font-family: "PT Sans", sans-serif; }

  .letterhead {
    position: absolute; left: 330px; top: 15px;
    width: 540px; height: 764px;
    background: var(--paper);
    box-shadow: 0 2px 10px rgba(0,0,0,0.12);
    overflow: hidden;
  }
  .header-swoosh { position: absolute; left: 0; top: 0; width: 540px; height: 130px; }

  .brand {
    position: absolute; right: 78px; top: 26px;
    display: flex; align-items: center; gap: 8px;
  }
  .brand-dot { width: 16px; height: 16px; border-radius: 50%; background: var(--brand-blue); }
  .brand-name {
    font-family: "Poppins", sans-serif; font-weight: 400;
    font-size: 25px; letter-spacing: 1px; color: var(--brand-blue); line-height: 1;
  }

  .letter {
    position: absolute; left: 54px; top: 140px; width: 430px;
    color: var(--ink);
    display: flex; flex-direction: column;
  }
  .letter-date { font-size: 10.5px; margin-bottom: 16px; }
  .recipient { font-size: 10.5px; line-height: 1.3; font-style: normal; margin-bottom: 12px; margin-left: 10px; }
  .salutation { font-size: 11.5px; font-weight: 700; margin-bottom: 12px; margin-left: 10px; }
  .letter-body p {
    font-size: 9.6px; line-height: 1.4; color: var(--body-ink);
    margin: 0 0 14px 10px;
  }

  .sign-off {
    align-self: flex-end;
    width: 170px; margin-top: 14px; margin-right: 8px;
    color: var(--ink);
  }
  .closing { font-size: 10.5px; margin-left: 14px; }
  .signature {
    font-family: "Nothing You Could Do", cursive;
    font-size: 24px; color: var(--signature-ink); line-height: 1.2; margin: 2px 0 2px;
  }
  .signer { font-size: 10.5px; line-height: 1.25; margin-left: 40px; }

  .contact-band {
    position: absolute; left: 0; bottom: 0; width: 540px; height: 30px;
    background: var(--brand-blue); color: var(--paper);
    display: flex; align-items: center; gap: 6px;
    padding-left: 28px; font-size: 10px; white-space: nowrap;
  }
  .contact-item { display: flex; align-items: center; gap: 4px; }
  .contact-icon { width: 11px; height: 11px; flex: none; }
</style>
</head>
<body>
  <main class="letterhead">
    <svg class="header-swoosh" viewBox="0 0 540 130" aria-hidden="true">
      <path fill="var(--soft-grey)" d="M0,48 C70,58 150,72 250,70 C150,80 70,72 0,62 Z"/>
      <path fill="var(--brand-grey)" d="M290,60 C380,58 460,52 540,38 L540,50 C460,62 380,66 290,60 Z"/>
      <path fill="var(--brand-blue)" d="M0,36 C90,48 170,70 260,72 C360,74 450,64 540,52 L540,64 C450,78 360,86 260,84 C170,82 90,62 0,46 Z"/>
    </svg>

    <div class="brand">
      <span class="brand-dot"></span>
      <span class="brand-name">HALVERN</span>
    </div>

    <section class="letter">
      <p class="letter-date">January 03, 2017</p>
      <address class="recipient">
        Mr. John Doe<br>
        President<br>
        AA Corporation<br>
        111 Street Name, Suite#<br>
        City, State, 12345
      </address>
      <p class="salutation">Dear Mr. John,</p>
      <div class="letter-body">
        <p>Lorem Ipsum is simply dummy text of the printing and typesetting industry. Lorem Ipsum has been the industry's standard dummy text ever since the 1500s, when an unknown printer took a galley of type and scrambled it to make a type specimen book. It has survived not only five centuries, but also the leap into electronic typesetting, remaining essentially unchanged.</p>
        <p>The standard chunk of Lorem Ipsum used since the 1500s is reproduced below for those interested. Sections 1.10.32 and 1.10.33 from "de Finibus Bonorum et Malorum" by Cicero are also reproduced in their exact original form, accompanied by English versions from the 1914 translation by H. Rackham</p>
        <p>Lorem Ipsum is simply dummy text of the printing and typesetting industry. Lorem Ipsum has been the industry's standard dummy text ever since the 1500s, when an unknown printer took a galley of type and scrambled it to make a type specimen book. It has survived not only five centuries, but also the leap into electronic typesetting, remaining essentially unchanged. It was popularised in the</p>
      </div>

      <div class="sign-off">
        <p class="closing">Sincerely Your,</p>
        <p class="signature">your name</p>
        <p class="signer">Name Last Name<br>Company Name</p>
      </div>
    </section>

    <footer class="contact-band">
      <span class="contact-item">
        <svg class="contact-icon" viewBox="0 0 12 12" aria-hidden="true"><circle cx="6" cy="6" r="6" fill="#fff"/><path d="M6 2.3a2.2 2.2 0 0 0-2.2 2.2C3.8 6.2 6 9.4 6 9.4s2.2-3.2 2.2-4.9A2.2 2.2 0 0 0 6 2.3zm0 3a.8.8 0 1 1 0-1.6.8.8 0 0 1 0 1.6z" fill="var(--brand-blue)"/></svg>
        482 W 71st Street, 14th Floor New York, NY 10157
      </span>
      <span class="contact-item">
        <svg class="contact-icon" viewBox="0 0 12 12" aria-hidden="true"><circle cx="6" cy="6" r="6" fill="#fff"/><path d="M4.2 2.8l1 1.5-.6.7c.4.9 1.1 1.6 2 2l.7-.6 1.5 1-.5 1.1c-2.5-.2-4.5-2.2-4.7-4.7z" fill="var(--brand-blue)"/></svg>
        +1 (212) 555 0147
      </span>
      <span class="contact-item">
        <svg class="contact-icon" viewBox="0 0 12 12" aria-hidden="true"><circle cx="6" cy="6" r="6" fill="#fff"/><rect x="3" y="5" width="6" height="3.4" rx=".5" fill="var(--brand-blue)"/><rect x="4" y="2.8" width="4" height="2" fill="var(--brand-blue)"/></svg>
        +1 (212) 555 0182
      </span>
    </footer>
  </main>
</body>
</html>
```